Launching new podcast and need artwork

we are two guys in our early 40's from east Texas who are starting a podcast around personal finance.

The title of the podcast will be "Ledger Gripes" and the subtitle will be "Financial hacks with some southern charm"

We own the company boundlessdaysplanning.example and will be using the podcast as a lead generation for our primary business of financial coaching.

Target Market(s)

Male 35-45 years old

Industry/Entity Type

Personal finance

Requirements
Nice to have
• Rugged or rustic feel would fit our personas

```html
<!DOCTYPE html>
<html lang="en">
<head>
<meta charset="utf-8">
<title>Ledger Gripes Podcast Cover</title>
<link rel="stylesheet" href="https://fonts.googleapis.com/css2?family=Anton&family=Poppins:wght@500;600;700&display=swap">
<style>
  :root {
    --stage: #dcdcdc;
    --paper: #ffffff;
    --navy: #0b1f5e;
    --royal-deep: #08226f;
    --royal: #0c3aa6;
    --green: #8bc43f;
    --brand-blue: #3b66ad;
    --white: #ffffff;
  }
  html, body {
    margin: 0;
    padding: 0;
    width: 1086px;
    height: 1200px;
    overflow: hidden;
    background: var(--stage);
  }
  .cover {
    position: absolute;
    left: 107px;
    top: 164px;
    width: 872px;
    height: 872px;
    background: var(--paper);
    overflow: hidden;
  }
  .brand-name {
    position: absolute;
    top: 118px;
    left: 0;
    width: 100%;
    text-align: center;
    font-family: "Poppins", sans-serif;
    font-weight: 600;
    font-size: 22px;
    letter-spacing: 3px;
    color: var(--brand-blue);
  }
  .brand-mark {
    position: absolute;
    left: 421px;
    top: 74px;
    width: 30px;
    height: 30px;
    background: var(--brand-blue);
  }
  .market-band {
    position: absolute;
    left: 0;
    top: 392px;
    width: 100%;
    height: 480px;
    background: linear-gradient(180deg, var(--royal-deep) 0%, #0a2f8f 55%, var(--royal) 100%);
  }
  .market-chart {
    position: absolute;
    left: 0;
    top: 0;
    width: 872px;
    height: 480px;
  }
  .title {
    position: absolute;
    left: 0;
    top: 0;
    width: 872px;
    height: 872px;
  }
  .title-top { font-family: "Anton", sans-serif; fill: var(--navy); }
  .title-bottom { font-family: "Anton", sans-serif; fill: var(--green); }
  .tagline {
    position: absolute;
    left: 0;
    width: 100%;
    text-align: center;
    color: var(--white);
    font-family: "Poppins", sans-serif;
    margin: 0;
  }
  .tagline-lead { top: 660px; font-weight: 500; font-size: 39px; letter-spacing: -0.5px; }
  .tagline-accent { top: 705px; font-weight: 700; font-size: 50px; letter-spacing: -0.5px; }
  .format-label {
    position: absolute;
    top: 803px;
    left: 0;
    width: 100%;
    text-align: center;
    color: var(--white);
    font-family: "Poppins", sans-serif;
    font-weight: 500;
    font-size: 17px;
    letter-spacing: 5px;
    margin: 0;
  }
</style>
</head>
<body>
  <main class="cover">
    <div class="brand-mark" aria-hidden="true"></div>
    <div class="brand-name">BOUNDLESS DAYS PLANNING</div>

    <section class="market-band">
      <svg class="market-chart" viewBox="0 0 872 480" aria-hidden="true">
        <g fill="#1a4cc0" opacity="0.35">
          <rect x="10" y="160" width="14" height="100"/>
          <rect x="40" y="190" width="14" height="70"/>
          <rect x="70" y="140" width="14" height="120"/>
          <rect x="100" y="175" width="14" height="85"/>
          <rect x="130" y="120" width="14" height="140"/>
          <rect x="160" y="150" width="14" height="110"/>
          <rect x="200" y="100" width="14" height="160"/>
          <rect x="420" y="80" width="14" height="180"/>
          <rect x="460" y="130" width="14" height="130"/>
          <rect x="700" y="140" width="14" height="120"/>
          <rect x="730" y="110" width="14" height="150"/>
          <rect x="760" y="170" width="14" height="90"/>
          <rect x="790" y="95" width="14" height="165"/>
          <rect x="820" y="150" width="14" height="110"/>
          <rect x="850" y="120" width="14" height="140"/>
        </g>
        <path d="M0 60 C80 40 120 110 200 80 S330 20 430 60 S560 70 620 60 S760 10 872 0" fill="none" stroke="#3fa080" stroke-width="1.5" opacity="0.55"/>
        <path d="M0 100 C90 120 150 60 240 70 S380 100 480 90 S640 30 872 50" fill="none" stroke="#3a6fe0" stroke-width="1.2" opacity="0.5"/>
        <line x1="0" y1="260" x2="872" y2="260" stroke="#2a63e0" stroke-width="2" opacity="0.7"/>
        <g stroke="#2a5ad0" stroke-width="1" opacity="0.3">
          <line x1="0" y1="300" x2="872" y2="300"/>
          <line x1="0" y1="350" x2="872" y2="350"/>
          <line x1="0" y1="410" x2="872" y2="410"/>
          <line x1="436" y1="260" x2="436" y2="480"/>
          <line x1="330" y1="260" x2="200" y2="480"/>
          <line x1="540" y1="260" x2="670" y2="480"/>
          <line x1="220" y1="260" x2="-40" y2="480"/>
          <line x1="650" y1="260" x2="910" y2="480"/>
        </g>
      </svg>
    </section>

    <svg class="title" viewBox="0 0 872 872" role="img" aria-label="Ledger Gripes">
      <defs>
        <clipPath id="paper-zone"><rect x="0" y="0" width="872" height="392"/></clipPath>
      </defs>
      <text class="title-top" clip-path="url(#paper-zone)" x="139" y="400" font-size="252" textLength="592" lengthAdjust="spacingAndGlyphs">LEDGER</text>
      <text class="title-bottom" x="139" y="641" font-size="322" textLength="592" lengthAdjust="spacingAndGlyphs">GRIPE$</text>
    </svg>

    <p class="tagline tagline-lead">FINANCIAL HACKS WITH SOME</p>
    <p class="tagline tagline-accent">SOUTHERN CHARM</p>
    <p class="format-label">PODCAST</p>
  </main>
</body>
</html>
```